Accounting firm needing business card / letterhead designed
Marcus T. Elbering, CPA
marcus@fernquill.com
www.fernquill.com
482 N Harlow Ave Larkford, OH 43719
419-555-0172

```html
<!DOCTYPE html>
<html lang="en">
<head>
<meta charset="utf-8">
<title>Fernquill — Business Card</title>
<link rel="stylesheet" href="https://fonts.googleapis.com/css2?family=Fredoka:wght@500;600&display=swap">
<style>
  :root {
    --navy: #26225f;
    --green: #8dc63f;
    --fold: #8a86b6;
    --white: #ffffff;
    --edge: #e4ecd8;
  }
  * { margin: 0; padding: 0; box-sizing: border-box; }
  html, body { width: 1200px; height: 1000px; overflow: hidden; background: var(--white); }
  body { position: relative; font-family: "Fredoka", "Arial Rounded MT Bold", sans-serif; }

  .card {
    position: absolute;
    width: 530px;
    background: var(--white);
    border: 1px solid var(--edge);
    overflow: hidden;
  }
  .card--front { left: 41px; top: 45px; height: 885px; }
  .card--back  { left: 636px; top: 45px; height: 883px; }
  .card__shapes { position: absolute; inset: 0; }

  .wordmark {
    position: absolute;
    left: 0; right: 0;
    text-align: center;
    color: var(--navy);
    font-weight: 600;
    line-height: 1;
    white-space: nowrap;
  }
  .card--front .wordmark { top: 156px; font-size: 38px; letter-spacing: 3px; }
  .card--back  .wordmark { top: 350px; font-size: 54px; letter-spacing: 4px; }

  .holder {
    position: absolute;
    left: 0; right: 0; top: 425px;
    text-align: center;
    color: var(--white);
  }
  .holder__name { font-size: 22px; font-weight: 600; line-height: 1.1; }
  .holder__title { font-size: 13px; font-weight: 600; margin-top: 3px; }

  .contact-list { position: absolute; left: 78px; top: 566px; list-style: none; }
  .contact-list__item {
    display: flex; align-items: center;
    height: 28px; margin-bottom: 19px;
    color: var(--white); font-size: 19px; font-weight: 600;
    white-space: nowrap;
  }
  .contact-list__icon { width: 26px; height: 26px; margin-right: 18px; flex: none; }

  .site-tag {
    position: absolute; left: 0; right: 0; top: 772px;
    display: flex; justify-content: center; align-items: center;
    color: var(--white); font-size: 20px; font-weight: 600;
  }
  .site-tag__icon { width: 19px; height: 19px; margin-right: 12px; }
</style>
</head>
<body>

<section class="card card--front">
  <svg class="card__shapes" width="530" height="885" viewBox="0 0 530 885">
    <rect x="0" y="428" width="530" height="457" fill="var(--green)"/>
    <polygon points="57,428 74,408 74,428" fill="var(--fold)"/>
    <polygon points="456,408 473,428 456,428" fill="var(--fold)"/>
    <polygon points="74,408 456,408 426,490 103,490" fill="var(--navy)"/>
  </svg>

  <div class="wordmark">FERNQUILL</div>

  <div class="holder">
    <div class="holder__name">Marcus T. Elbering</div>
    <div class="holder__title">CPA</div>
  </div>

  <ul class="contact-list">
    <li class="contact-list__item">
      <svg class="contact-list__icon" viewBox="0 0 26 26">
        <path d="M2 9c0-3 5-5 11-5s11 2 11 5v2h-5V8H7v3H2z" fill="var(--navy)"/>
        <path d="M6 12h14l3 10H3z" fill="var(--navy)"/>
        <circle cx="13" cy="17" r="3" fill="var(--green)"/>
      </svg>
      555 555 0172
    </li>
    <li class="contact-list__item">
      <svg class="contact-list__icon" viewBox="0 0 26 26">
        <rect x="2" y="5" width="22" height="16" fill="none" stroke="var(--navy)" stroke-width="2"/>
        <path d="M2 5l11 9 11-9M2 21l8-8M24 21l-8-8" fill="none" stroke="var(--navy)" stroke-width="2"/>
      </svg>
      marcus@fernquill.com
    </li>
    <li class="contact-list__item">
      <svg class="contact-list__icon" viewBox="0 0 26 26" fill="none" stroke="var(--navy)" stroke-width="2">
        <circle cx="13" cy="13" r="11"/>
        <ellipse cx="13" cy="13" rx="5" ry="11"/>
        <path d="M2 13h22M4 7h18M4 19h18"/>
      </svg>
      www.fernquill.com
    </li>
    <li class="contact-list__item">
      <svg class="contact-list__icon" viewBox="0 0 26 26">
        <path d="M13 2L1 13h4v11h6v-7h4v7h6V13h4z" fill="var(--navy)"/>
      </svg>
      482 N Harlow Ave Larkford, OH 43719
    </li>
  </ul>
</section>

<section class="card card--back">
  <svg class="card__shapes" width="530" height="883" viewBox="0 0 530 883">
    <rect x="0" y="763" width="530" height="120" fill="var(--green)"/>
    <polygon points="56,763 73,743 73,763" fill="var(--fold)"/>
    <polygon points="456,743 473,763 456,763" fill="var(--fold)"/>
    <polygon points="73,743 456,743 420,825 102,825" fill="var(--navy)"/>
  </svg>

  <div class="wordmark">FERNQUILL</div>

  <div class="site-tag">
    <svg class="site-tag__icon" viewBox="0 0 18 18" fill="none" stroke="var(--green)" stroke-width="1.8">
      <circle cx="9" cy="9" r="7.5"/>
      <path d="M4 4c3 2 4 5 2 10M11 2c-1 4 1 6 5 7M2 10c4-1 7 0 9 6"/>
    </svg>
    www.fernquill.com
  </div>
</section>

</body>
</html>
```